Redesign Website for Tandara Flame

I have an existing website on https://www.tandaraflame-example.com.au/ and would like to have this redesigned professionally with new content (please refer to word document). We are fire protection engineers providing fire services design expertise and engineering design to a range of different clients.

We also provide drafting services to clients in the form of completing final commissioning documentation such as 'as-installed' drawings and fire services block plans to ensure compliance with the building code and relevant Australian Standards.

Target Market(s)

Builders, Architects, Consultants, Project Managers

Industry/Entity Type

Engineering Consultant

Coding

Coded - Design and coding required

Number of Pages Required

4 page

Font styles to use
Sans Serif

Requirements
Must have
• Home and about Page, fire services design page, fire block plans page, contact us page (4 Pages).

The website colour choice must match or compliment the new company logo.
Nice to have
• Quality photos of fire services installations in buildings to Australian Standards.

A website similar to this would be ideal http://corbellpyro-example.com.au
Should not have
• Stolen licensed photos

```html
<!DOCTYPE html>
<html lang="en">
<head>
<meta charset="utf-8">
<title>Tandara Flame – Fire Protection Solutions</title>
<link href="https://fonts.googleapis.com/css2?family=Montserrat:wght@400;500;600;700;800&display=swap" rel="stylesheet">
<style>
:root{
  --orange:#f28a1c;
  --orange-deep:#e9780e;
  --dark:#2a2a2a;
  --darker:#1c1c1c;
  --ink:#222;
  --grey-text:#6b6b6b;
  --light:#f2f2f2;
  --white:#fff;
}
*{margin:0;padding:0;box-sizing:border-box}
html,body{width:1200px;height:3599px;overflow:hidden}
body{font-family:'Montserrat',sans-serif;color:var(--ink);position:relative;background:var(--white)}
.abs{position:absolute}
.center{left:0;width:1200px;text-align:center}
.brand-dot{display:inline-block;border-radius:50%;border:3px solid var(--orange)}
.btn{position:absolute;height:38px;background:var(--orange);color:var(--white);font-weight:700;font-size:15px;display:flex;align-items:center;padding-left:19px;border-radius:2px}
.btn .dot{position:absolute;right:-22px;top:-2px;width:42px;height:42px;border-radius:50%;background:var(--white);border:3px solid var(--orange)}
.divider{position:absolute;left:450px;width:300px;height:10px}
.divider::before{content:"";position:absolute;left:0;right:0;top:4px;height:2px;background:linear-gradient(90deg,transparent,var(--orange) 30%,var(--orange) 45%,transparent 45%,transparent 55%,var(--orange) 55%,var(--orange) 70%,transparent)}
.divider::after{content:"";position:absolute;left:146px;top:1px;width:8px;height:8px;border-radius:50%;background:var(--white)}
.divider.dark::after{background:#111}
/* hero */
.hero{top:0;left:0;width:1200px;height:670px;background:radial-gradient(ellipse at 50% 40%,#4a4a4a 0%,#2b2b2b 55%,#161616 100%)}
.hero-name{top:262px;font-size:44px;font-weight:600;color:var(--orange);letter-spacing:1px}
.hero-title{top:352px;font-size:45px;font-weight:800;color:var(--white)}
.hero-sub{top:418px;font-size:18px;font-weight:600;color:var(--white);line-height:21px}
.mouse{left:590px;top:622px;width:20px;height:30px;border:2px solid #ddd;border-radius:10px}
/* nav */
.nav{top:670px;left:0;width:1200px;height:108px;background:var(--dark)}
.nav-orange{top:670px;left:324px;width:876px;height:108px;background:var(--orange);clip-path:polygon(0 0,100% 0,100% 100%,60px 100%)}
.nav-name{left:35px;top:706px;font-size:33px;font-weight:600;color:var(--orange)}
.nav-links{left:412px;top:716px;display:flex;gap:14px;align-items:center;font-size:16px;font-weight:600;color:var(--white)}
.nav-links span.sep{width:4px;height:4px;border-radius:50%;background:var(--white)}
/* about */
.about{top:778px;left:0;width:1200px;height:549px;background:var(--light)}
.welcome{left:98px;top:840px;font-size:31px;color:var(--grey-text)}
.about-name{left:96px;top:878px;font-size:58px;font-weight:800;color:var(--orange)}
.about-copy{left:98px;top:958px;width:476px;font-size:13px;line-height:17.4px;text-align:justify;color:#333}
.about-copy p+p{margin-top:17px}
.about-photo{left:622px;top:848px;width:476px;height:416px}
/* services */
.services{top:1327px;left:0;width:1200px;height:808px;background:linear-gradient(180deg,#262626,#1d1d1d)}
.sec-mark{left:575px;width:50px;height:50px}
.sec-title{font-size:45px;font-weight:800;color:var(--orange)}
.services-intro{top:1561px;font-size:14.5px;font-weight:600;color:var(--white);line-height:18px}
.hex{position:absolute;width:175px;height:198px;color:var(--white);text-align:center}
.hex svg.shape{position:absolute;left:0;top:0}
.hex .num{position:absolute;left:0;right:0;top:26px;font-size:25px;font-weight:700;color:#4a4a4a}
.hex .label{position:absolute;left:10px;right:10px;top:80px;font-size:14px;font-weight:700;line-height:17px}
.hex svg.icon{position:absolute;left:70px;top:136px}
.notch{left:560px;top:2114px;width:80px;height:30px;background:var(--white);border-radius:40px 40px 0 0}
/* block plans */
.plans-copy{top:2362px;left:140px;width:920px;text-align:center;font-size:18.5px;line-height:27px;color:#333}
/* contact */
.contact{top:2640px;left:0;width:1200px;height:720px;background:linear-gradient(180deg,var(--orange),var(--orange-deep))}
.contact-title{top:2762px;font-size:45px;font-weight:800;color:var(--white)}
.field{position:absolute;background:var(--white);border:1px solid #ddd;border-radius:2px;font-size:11px;color:#999;padding:12px 11px}
.send{left:210px;top:3092px;width:778px;height:42px;background:#0d0d0d;color:var(--white);font-size:12px;font-weight:700;display:flex;align-items:center;justify-content:center}
.curve{top:3170px;left:0}
/* footer */
.foot-head{font-size:17px;font-weight:600;color:var(--orange);text-decoration:underline;text-decoration-thickness:1px;text-underline-offset:6px}
.foot-links{left:98px;top:3360px;font-size:15px;line-height:25px;color:#222}
.foot-contact{left:360px;top:3360px;font-size:15px;line-height:19px;color:#222}
.foot-contact .row{position:relative;padding-left:30px;margin-bottom:21px}
.foot-contact svg{position:absolute;left:0;top:1px}
.foot-name{left:762px;top:3430px;font-size:43px;font-weight:600;color:var(--orange)}
.bottom{top:3535px;left:0;width:1200px;height:64px;background:var(--darker)}
.copyright{left:98px;top:3556px;font-size:14px;font-weight:600;color:var(--white)}
.social{top:3547px;width:34px;height:34px;border-radius:50%;background:var(--orange)}
</style>
</head>
<body>

<!-- hero -->
<div class="abs hero" role="img" aria-label="Photograph of an underground car park with fire services pipework"></div>
<div class="abs" style="left:563px;top:150px;width:74px;height:74px"><span class="brand-dot" style="width:74px;height:74px"></span></div>
<div class="abs center hero-name">TANDARA FLAME</div>
<h1 class="abs center hero-title">FIRE PROTECTION SOLUTIONS</h1>
<p class="abs center hero-sub">Focused on ensuring your Fire Safety Assets<br>are properly Installed and Maintained.<br>Your safety is our top priority.</p>
<a class="btn" style="left:535px;top:514px;width:136px">Contact Us<span class="dot"></span></a>
<div class="abs mouse"></div>

<!-- nav -->
<div class="abs nav"></div>
<div class="abs nav-orange"></div>
<div class="abs nav-name">TANDARA FLAME</div>
<nav class="abs nav-links">
  <svg width="26" height="22" viewBox="0 0 26 22"><path d="M13 1 1 11h3v10h7v-6h4v6h7V11h3z" fill="#fff"/></svg>
  <span class="sep"></span><span>ABOUT US</span><span class="sep"></span><span>FIRE SERVICES DESIGN</span><span class="sep"></span><span>FIRE BLOCK PLANS</span><span class="sep"></span><span>CONTACT US</span>
  <svg style="margin-left:24px" width="16" height="16" viewBox="0 0 16 16"><circle cx="6.5" cy="6.5" r="5" stroke="#fff" stroke-width="2" fill="none"/><path d="m10 10 5 5" stroke="#fff" stroke-width="2"/></svg>
</nav>

<!-- about -->
<div class="abs about"></div>
<div class="abs" style="left:190px;top:778px;width:820px;height:22px;background:radial-gradient(ellipse at 50% 0,rgba(0,0,0,.25),transparent 70%)"></div>
<div class="abs welcome">Welcome to the</div>
<h2 class="abs about-name">TANDARA FLAME</h2>
<div class="abs about-copy">
  <p>Tandara Flame is a company based in Sydney providing the Australian market expertise in the field of fire safety. Our mission is to assist builders, architects, fire contractors, consultants and project managers with the preparation of fire services design and specifications to meet regulatory requirements for Complying Development Certificate (CDC), Development Applications (DA) or Council Fire Orders.</p>
  <p>We also provide fire services design peer review and sign-off under the new Fire Services Design (FSD) class of the Fire Protection Accreditation Scheme (FPAS) and the preparation of a Clause 164B objection letter to exempt certain building work on fire safety systems be exempt from compliance with the BCA and relevant standards.</p>
</div>
<a class="btn" style="left:98px;top:1225px;width:132px">Know More<span class="dot"></span></a>
<svg class="abs about-photo" viewBox="0 0 476 416">
  <defs><linearGradient id="pg" x1="0" y1="0" x2="1" y2="1"><stop offset="0" stop-color="#d9d9d6"/><stop offset=".5" stop-color="#a8403a"/><stop offset="1" stop-color="#7d7d7b"/></linearGradient></defs>
  <polygon points="119,0 357,0 476,208 357,416 119,416 0,208" fill="#fff" style="filter:drop-shadow(0 4px 10px rgba(0,0,0,.25))"/>
  <polygon points="125,12 351,12 462,208 351,404 125,404 14,208" fill="url(#pg)" role="img" aria-label="Photograph of red fire pump controllers in a plant room"/>
</svg>

<!-- fire services design -->
<div class="abs services"></div>
<div class="abs sec-mark" style="top:1379px"><span class="brand-dot" style="width:50px;height:50px"></span></div>
<h2 class="abs center sec-title" style="top:1449px">FIRE SERVICES DESIGN</h2>
<div class="divider dark" style="top:1511px"></div>
<p class="abs center services-intro">We have proficient knowledge and capabilities in the preparation of fire services design and specifications relating<br>to the below fire safety systems:</p>

<!-- hex cells -->
<div class="hex" style="left:99px;top:1625px"><svg class="shape" width="175" height="198"><polygon points="87.5,2 173,51 173,147 87.5,196 2,147 2,51" fill="#0e0e0e" stroke="#444" stroke-width="2"/></svg><div class="num">01</div><div class="label">Smoke<br>Alarms</div><svg class="icon" width="36" height="30"><path d="M4 10h28v6a14 8 0 0 1-28 0z" fill="var(--orange)"/><rect x="6" y="6" width="24" height="4" fill="var(--orange)"/></svg></div>
<div class="hex" style="left:306px;top:1625px"><svg class="shape" width="175" height="198"><polygon points="87.5,2 173,51 173,147 87.5,196 2,147 2,51" fill="#0e0e0e" stroke="#444" stroke-width="2"/></svg><div class="num">03</div><div class="label">Occupant<br>Warning Systems</div><svg class="icon" width="36" height="30"><rect x="2" y="2" width="32" height="20" fill="none" stroke="var(--orange)" stroke-width="3"/><path d="M13 28h10M18 22v6" stroke="var(--orange)" stroke-width="3"/><path d="M18 7l5 9h-10z" fill="var(--orange)"/></svg></div>
<div class="hex" style="left:513px;top:1625px"><svg class="shape" width="175" height="198"><polygon points="87.5,2 173,51 173,147 87.5,196 2,147 2,51" fill="#0e0e0e" stroke="#444" stroke-width="2"/></svg><div class="num">05</div><div class="label">Fire<br>Hose Reels</div><svg class="icon" width="36" height="36"><path d="M4 4v22M9 4v22M14 4v22M19 4v22" stroke="var(--orange)" stroke-width="3"/><circle cx="29" cy="14" r="5" fill="none" stroke="var(--orange)" stroke-width="3"/><path d="M11 26v8" stroke="var(--orange)" stroke-width="3"/></svg></div>
<div class="hex" style="left:718px;top:1625px"><svg class="shape" width="175" height="198"><polygon points="87.5,2 173,51 173,147 87.5,196 2,147 2,51" fill="#0e0e0e" stroke="#444" stroke-width="2"/></svg><div class="num">07</div><div class="label">Portable Fire<br>Extinguishers</div><svg class="icon" width="36" height="44"><rect x="12" y="12" width="13" height="30" rx="3" fill="var(--orange)"/><path d="M18 12V4h8M12 6l6-2" stroke="var(--orange)" stroke-width="3" fill="none"/></svg></div>
<div class="hex" style="left:925px;top:1625px"><svg class="shape" width="175" height="198"><polygon points="87.5,2 173,51 173,147 87.5,196 2,147 2,51" fill="#0e0e0e" stroke="#444" stroke-width="2"/></svg><div class="num">09</div><div class="label">Exit<br>Signs</div><svg class="icon" width="36" height="36"><rect x="3" y="3" width="30" height="30" fill="none" stroke="var(--orange)" stroke-width="3"/><path d="M14 28l4-9 5 3v6M18 19l1-6 6 4M12 15l6-2" stroke="var(--orange)" stroke-width="3" fill="none"/><circle cx="21" cy="9" r="2.5" fill="var(--orange)"/></svg></div>

<div class="hex" style="left:203px;top:1804px"><svg class="shape" width="175" height="198"><polygon points="87.5,2 173,51 173,147 87.5,196 2,147 2,51" fill="#0e0e0e" stroke="#444" stroke-width="2"/></svg><div class="num">02</div><div class="label" style="top:74px">Automatic Smoke<br>Detection and<br>Alarm Systems</div><svg class="icon" width="36" height="32"><path d="M10 26a8 12 0 0 1 16 0z" fill="var(--orange)"/><path d="M4 10a16 16 0 0 0 0 14M32 10a16 16 0 0 1 0 14" stroke="var(--orange)" stroke-width="3" fill="none"/><rect x="8" y="26" width="20" height="3" fill="var(--orange)"/></svg></div>
<div class="hex" style="left:409px;top:1804px"><svg class="shape" width="175" height="198"><polygon points="87.5,2 173,51 173,147 87.5,196 2,147 2,51" fill="#0e0e0e" stroke="#444" stroke-width="2"/></svg><div class="num">04</div><div class="label" style="top:74px">Emergency Warning<br>and Intercom<br>System (EWIS)</div><svg class="icon" width="40" height="32"><rect x="2" y="2" width="26" height="26" fill="none" stroke="var(--orange)" stroke-width="3"/><circle cx="15" cy="13" r="4" fill="var(--orange)"/><path d="M8 25a7 6 0 0 1 14 0z" fill="var(--orange)"/><rect x="31" y="6" width="7" height="22" fill="var(--orange)"/></svg></div>
<div class="hex" style="left:616px;top:1804px"><svg class="shape" width="175" height="198"><polygon points="87.5,2 173,51 173,147 87.5,196 2,147 2,51" fill="#0e0e0e" stroke="#444" stroke-width="2"/></svg><div class="num">06</div><div class="label">Fire<br>Hydrants</div><svg class="icon" width="36" height="40"><path d="M12 10a6 6 0 0 1 12 0z" fill="var(--orange)"/><rect x="10" y="10" width="16" height="26" fill="var(--orange)"/><rect x="5" y="18" width="26" height="7" fill="var(--orange)"/><circle cx="18" cy="22" r="3" fill="#0e0e0e"/></svg></div>
<div class="hex" style="left:821px;top:1804px"><svg class="shape" width="175" height="198"><polygon points="87.5,2 173,51 173,147 87.5,196 2,147 2,51" fill="#0e0e0e" stroke="#444" stroke-width="2"/></svg><div class="num">08</div><div class="label">Emergency<br>Lighting</div><svg class="icon" width="36" height="36"><path d="M9 28a9 11 0 0 1 18 0z" fill="var(--orange)"/><rect x="4" y="29" width="28" height="4" fill="var(--orange)"/><path d="M18 2v7M5 8l5 5M31 8l-5 5" stroke="var(--orange)" stroke-width="3"/></svg></div>

<a class="btn" style="left:526px;top:2035px;width:136px">Know More<span class="dot"></span></a>
<div class="abs notch"></div>
<svg class="abs" style="left:590px;top:2135px" width="20" height="12"><path d="M3 2l7 7 7-7" stroke="#222" stroke-width="2.5" fill="none"/></svg>

<!-- fire block plans -->
<div class="abs sec-mark" style="top:2192px"><span class="brand-dot" style="width:50px;height:50px"></span></div>
<h2 class="abs center sec-title" style="top:2259px">FIRE BLOCK PLANS</h2>
<div class="divider" style="top:2321px"></div>
<p class="abs plans-copy">We can also assist our clients in the preparation commissioning documentation (i.e. zone block plan, fire hydrant block plans, sprinkler block plan) as required for relevant fire safety systems on completion of a project to achieve full compliance with relevant Australian Standards for project handover or for the update of existing outdated / missing block plans.</p>
<a class="btn" style="left:526px;top:2511px;width:136px">Know More<span class="dot"></span></a>

<!-- get in touch -->
<div class="abs contact" role="img" aria-label="Orange-tinted photograph of fire sprinkler pipework"></div>
<div class="abs sec-mark" style="top:2692px"><span class="brand-dot" style="width:50px;height:50px;border-color:#fff"></span></div>
<h2 class="abs center contact-title">GET IN TOUCH</h2>
<div class="divider dark" style="top:2821px;filter:brightness(10)"></div>
<div class="field" style="left:210px;top:2857px;width:377px;height:42px">FIRST NAME*</div>
<div class="field" style="left:614px;top:2857px;width:374px;height:42px">LAST NAME*</div>
<div class="field" style="left:210px;top:2907px;width:377px;height:42px">E-MAIL ADDRESS*</div>
<div class="field" style="left:614px;top:2907px;width:374px;height:42px">PHONE NUMBER*</div>
<div class="field" style="left:210px;top:2957px;width:778px;height:127px">MESSAGE</div>
<div class="abs send">SEND NOW</div>

<svg class="abs curve" width="1200" height="365" viewBox="0 0 1200 365">
  <path d="M0 140Q600 -30 1200 140V365H0z" fill="#fff"/>
  <path d="M0 140Q600 -30 1200 140" stroke="#111" stroke-width="5" fill="none"/>
</svg>

<!-- footer -->
<div class="abs" style="left:577px;top:3253px;width:46px;height:46px"><span class="brand-dot" style="width:46px;height:46px"></span></div>
<div class="abs foot-head" style="left:98px;top:3314px">QUICK LINKS</div>
<div class="abs foot-head" style="left:390px;top:3314px">CONTACT US</div>
<div class="abs foot-links">Home<br>About Us<br>Fire services design<br>Fire block plans<br>Contact us</div>
<div class="abs foot-contact">
  <div class="row"><svg width="18" height="20"><path d="M9 1a7 7 0 0 0-7 7c0 5 7 11 7 11s7-6 7-11a7 7 0 0 0-7-7z" fill="var(--orange)"/><circle cx="9" cy="8" r="2.5" fill="#fff"/></svg>Level 1 / 100 Marlow Street, Sydney NSW 0000<br>GPO BOX 4120 Sydney NSW 2001</div>
  <div class="row"><svg width="18" height="18"><circle cx="9" cy="9" r="9" fill="var(--orange)"/><path d="M6 5l2 3-1 1q1 2 3 3l1-1 3 2-1 2q-6-1-8-8z" fill="#fff"/></svg>(02) 5550 1934</div>
  <div class="row"><svg width="18" height="18"><circle cx="9" cy="9" r="9" fill="var(--orange)"/><rect x="4" y="6" width="10" height="7" fill="none" stroke="#fff" stroke-width="1.4"/><path d="M4 6l5 4 5-4" stroke="#fff" stroke-width="1.4" fill="none"/></svg>info@tandaraflame-example.com.au</div>
</div>
<div class="abs" style="left:870px;top:3325px;width:100px;height:100px"><span class="brand-dot" style="width:100px;height:100px;border-width:5px"></span></div>
<div class="abs foot-name">TANDARA FLAME</div>

<div class="abs bottom"></div>
<div class="abs copyright">© COPYRIGHT - 2021 &nbsp;| &nbsp;ALL RIGHTS RESERVED</div>
<span class="abs social" style="left:940px"></span>
<span class="abs social" style="left:983px"></span>
<span class="abs social" style="left:1025px"></span>
<span class="abs social" style="left:1067px"></span>

</body>
</html>
```